Kora_Plastering Web Design Project

Kora Plastering wants a modern looking 1 page website that clearly emphasises the 3 specialised construction services:
1. Plastering = (inside walls etc)
2. Rendering = (outside walls etc)
3. Cornicing = (inside wall and ceilings)

Kora Plastering is run by craftsmen, so be creative.

I really like http://quillnorth-example.com

The site design lends itself well to being a one pager - I like the html click thru panel (at the base above the fold) that allows reader to stay on the one page but can see see more info by tapping on the red arrows.

The site is also successful because it doesn't rely on photos - but makes the most of big headlines and client testimonials.

I could provide you with more content if you need it to achieve this kind of site.

Project Deadline Extended
Reason: Hi, we have decided to extend the deadline as we have only received ideas from one designer. We feel there is still scope to improve on the designs we have received so far. Improvements in the following areas: - design that complements the new logo design (the logo shows that KORA provide services inside and outside the house) - the design doesn't look like one of the many 'template' designs you see these days - the design does not need to use photos - if you can illustrate well as well as design website you will have an advantage! - site should look very modern / up to date We have now guaranteed payment in case designers were holding off.

Target Market(s)

Architects, interior designers, builders, home owners

Industry/Entity Type

Construction

Requirements
Must have
• Design at 1024 x 768
Website design should complement new logo - with black and ivory being dominant colours. (Logo is attached)
The site should be creative - as creativity is one of the key aspects of the service provide by Kora Plastering.
Text for the site has been provided - see pdf
Nice to have
• It's not essential to use photos. In the quick example I have attached I have sourced photos from snapverde-example.com
File #: 8302947 / File #: 40918526 / File #: 9175382. I repeat photos are not mandatory - you may prefer to use other graphical devices.
Easily coded
Modern looking design

```html
<!DOCTYPE html>
<html lang="en">
<head>
<meta charset="utf-8">
<title>Kora Plastering</title>
<link rel="stylesheet" href="https://fonts.googleapis.com/css2?family=Fjalla+One&family=Arimo:wght@400;700&display=swap">
<style>
:root{
  --ink:#201a17;
  --ivory:#fcf4d0;
  --olive:#7a7650;
  --olive-dark:#6f6a45;
  --logo:#f3ecd0;
  --muted:#a8a39c;
  --card-border:#d2d2d2;
  --page:#ececec;
}
*{margin:0;padding:0;box-sizing:border-box}
html,body{width:1200px;height:844px;overflow:hidden}
body{position:relative;background:#fff;font-family:"Arimo",Arial,sans-serif;color:#111}
.masthead{position:absolute;left:0;top:0;width:1200px;height:125px;background:var(--ink)}
.brand{position:absolute;left:139px;top:28px;display:flex;align-items:center;gap:12px;color:var(--logo);font-family:"Arimo",Arial,sans-serif;font-weight:700;letter-spacing:3px}
.brand-mark{width:14px;height:14px;background:var(--logo)}
.brand-name{font-size:30px;line-height:1.1}
.brand-name small{display:block;font-size:17px;letter-spacing:5px}
.cta{position:absolute;left:828px;width:227px;height:44px;border-radius:5px;background:linear-gradient(#fffdf2,#f6eab8);display:flex;align-items:center;padding-left:12px;gap:8px;text-decoration:none}
.cta.top{top:41px}
.cta.bottom{top:722px}
.cta-text{color:var(--olive);font-family:"Arimo",Arial,sans-serif;line-height:1}
.cta-text b{display:block;font-size:17px;letter-spacing:.3px}
.cta-text span{display:block;font-size:10px;margin-top:3px}
.intro{position:absolute;left:0;top:125px;width:1200px;height:225px;background:var(--ivory);box-shadow:0 2px 4px rgba(0,0,0,.25)}
.intro p{position:absolute;left:144px;top:21px;width:900px;font-family:"Fjalla One",sans-serif;font-size:31px;line-height:45px;color:var(--olive);text-shadow:2px 2px 3px rgba(0,0,0,.25)}
.services{position:absolute;left:0;top:350px;width:1200px;height:333px;background:var(--page);
  background-image:linear-gradient(rgba(255,255,255,.5) 1px,transparent 1px),linear-gradient(90deg,rgba(255,255,255,.5) 1px,transparent 1px);background-size:4px 4px}
.service{position:absolute;top:38px;width:267px;height:256px;border:1px solid var(--card-border);border-radius:6px;background:linear-gradient(#fff 45%,#eeeeee);box-shadow:0 1px 2px rgba(0,0,0,.1)}
.service:nth-child(1){left:139px}
.service:nth-child(2){left:467px}
.service:nth-child(3){left:788px}
.service-photo{margin:7px 6px 0;height:88px;border-radius:6px}
.photo-plaster{background:linear-gradient(90deg,#e6e6e4,#f4f4f2 50%,#dcdcd8)}
.photo-render{background:linear-gradient(160deg,#5fa6e6 0%,#a8c9e8 35%,#e0e0e0 60%,#c8c8c8)}
.photo-cornice{background:linear-gradient(180deg,#f0f0ee,#dedcd8 70%,#b8aa98)}
.service h2{font-weight:400;font-size:21px;color:var(--olive-dark);margin:10px 0 0 4px}
.service ul{list-style:none;margin:16px 0 0 4px}
.service li{position:relative;padding-left:13px;font-size:11.5px;line-height:13px;margin-bottom:14px;color:#111}
.service li::before{content:"»";position:absolute;left:0;top:-1px;font-size:11px;color:#444}
.our-work{position:absolute;left:0;top:683px;width:1200px;height:118px;background:var(--ink);border-top:2px solid #fff;border-bottom:2px solid #bbb}
.our-work h3{position:absolute;left:140px;top:24px;font-size:17px;color:#fff;font-weight:700}
.our-work hr{position:absolute;left:140px;top:48px;width:653px;border:0;border-top:1px solid #3a332f}
.our-work p{position:absolute;left:142px;top:60px;font-size:11.5px;line-height:17px;color:var(--muted);letter-spacing:.2px}
.legal{position:absolute;left:0;top:801px;width:1200px;height:43px;font-size:10.5px;color:#111}
.legal .copy{position:absolute;left:140px;top:14px}
.legal .contact{position:absolute;right:144px;top:15px}
</style>
</head>
<body>
<header class="masthead">
  <div class="brand"><span class="brand-mark"></span><span class="brand-name">KORA<small>PLASTERING</small></span></div>
  <a class="cta top" href="#contact">
    <svg width="32" height="28" viewBox="0 0 32 28"><rect x="1" y="3" width="30" height="22" rx="2" fill="#f3dca0" stroke="#c8a860"/><path d="M1 5 L16 16 L31 5" fill="none" stroke="#c8a860" stroke-width="1.5"/></svg>
    <span class="cta-text"><b>CONTACT US NOW</b><span>FOR AN OBLIGATION FREE QUOTE</span></span>
  </a>
</header>

<section class="intro">
  <p>We are specialists in all aspects of plastering, rendering and cornicing throughout Melbourne. We undertake residential and commercial projects of all sizes, including home renovations,new builds and specialised architectural projects.</p>
</section>

<section class="services">
  <article class="service">
    <div class="service-photo photo-plaster" role="img" aria-label="Photo of a freshly plastered empty white room"></div>
    <h2>Plastering</h2>
    <ul>
      <li>Solid plastering, including hard plaster, stucco, white set.</li>
      <li>Mouldings</li>
      <li>Plasterboard</li>
    </ul>
  </article>
  <article class="service">
    <div class="service-photo photo-render" role="img" aria-label="Photo of a rendered exterior wall with a ladder against blue sky"></div>
    <h2>Rendering</h2>
    <ul>
      <li>Cement render</li>
      <li>Acrylic render</li>
      <li>Specialised coatings</li>
    </ul>
  </article>
  <article class="service">
    <div class="service-photo photo-cornice" role="img" aria-label="Photo of a tradesman fitting a ceiling rose and cornice"></div>
    <h2>Cornicing</h2>
    <ul>
      <li>Custom &amp; off the shelf cornices</li>
      <li>Ornamental roses</li>
    </ul>
  </article>
</section>

<section class="our-work" id="contact">
  <h3>Our Work</h3>
  <hr>
  <p>We work inside and out and take pride in delivering a high quality finish across a diversity of traditional and modern styles.<br>We're always happy to provide advice andideas - and deliver a service that's prompt, neat and on budget.</p>
  <a class="cta bottom" href="#contact">
    <svg width="32" height="28" viewBox="0 0 32 28"><rect x="1" y="3" width="30" height="22" rx="2" fill="#f3dca0" stroke="#c8a860"/><path d="M1 5 L16 16 L31 5" fill="none" stroke="#c8a860" stroke-width="1.5"/></svg>
    <span class="cta-text"><b>CONTACT US NOW</b><span>FOR AN OBLIGATION FREE QUOTE</span></span>
  </a>
</section>

<footer class="legal">
  <span class="copy">Copyright © 2011 KORA Plastering. All rights reserved.</span>
  <span class="contact">KORA Plastering | Tel: 0412 835 610 | Email: info@koraplastering-example.com.au</span>
</footer>
</body>
</html>
```